Awesome Digital Ad Design – Pellucid Adreach

I am going to be setting up a Pellucid Adreach ad campaign I need creatives for.

Several sizes are needed in the end, however, please submit your design concept in the following 2 sizes to start:
Medium rectangle: 300X250
Leaderboard: 728X90

Original artwork/design files and images used expected upon payment and as part of the final delivery.

Ads should match our company brand and the information on this webpage: http://www.harborlyneworks.com/real-estate-marketing/
SEE MORE INSTRUCTIONS IN ATTACHED WORD DOC
Updates

Target Market(s)

Business-To-Business Audience –Real Estate Company Executives (Presidents/VPs/Owners/CEOs/Sales Managers).

Industry/Entity Type

Real Estate

Font styles to use
Sans Serif

Requirements
Must have
• Copy should be minimal words, billboard like. Please use real photos/images that would appeal to real estate high-level decision-maker executives.
Should not have
• No cartoons or graphics

```html
<!DOCTYPE html>
<html lang="en">
<head>
<meta charset="utf-8">
<title>Harborlyne Works – Display Ads</title>
<link rel="stylesheet" href="https://fonts.googleapis.com/css2?family=Oswald:wght@500;600&display=swap">
<style>
  :root {
    --board: #2d2d2d;
    --white: #ffffff;
    --maroon: #7a2637;
    --steel: #4f7488;
    --gold: #c9b47c;
    --orange: #f26a21;
    --orange-dark: #d9541a;
    --ink: #2a2a2a;
    --sky-light: #dfe6ef;
    --sky-mid: #9fb3cc;
    --sky-deep: #4f6d96;
    --sky-night: #2f4c78;
    --grey-band: #e6e7e9;
    --display: "Oswald", "Arial Narrow", sans-serif;
  }
  * { box-sizing: border-box; margin: 0; padding: 0; }
  html, body { width: 1200px; height: 1200px; overflow: hidden; }
  body { background: var(--board); position: relative; font-family: var(--display); }

  /* ---------- Medium rectangle ---------- */
  .ad-rectangle {
    position: absolute; left: 260px; top: 185px; width: 680px; height: 567px;
    background: var(--white); overflow: hidden;
  }
  .ad-rectangle .hero-photo {
    position: absolute; inset: 0;
    background:
      radial-gradient(ellipse 90px 210px at 420px 300px, rgba(47,76,120,0.85) 0%, rgba(63,95,143,0.55) 55%, rgba(79,109,150,0) 100%),
      radial-gradient(ellipse 200px 70px at 440px 480px, rgba(226,196,176,0.55) 0%, rgba(226,196,176,0) 100%),
      radial-gradient(ellipse 260px 340px at 470px 330px, rgba(159,179,204,0.5) 0%, rgba(159,179,204,0) 100%),
      linear-gradient(90deg, var(--white) 0%, var(--white) 26%, var(--sky-light) 42%, var(--sky-mid) 62%, var(--sky-deep) 100%);
  }
  .ad-rectangle .headline {
    position: absolute; left: 51px; top: 50px;
    color: var(--maroon); font-weight: 600; font-size: 44px; line-height: 56px; letter-spacing: 0.5px;
  }
  .ad-rectangle .ribbon { position: absolute; left: 0; top: 218px; width: 245px; height: 226px; }
  .ad-rectangle .ribbon-text {
    position: absolute; left: 66px; top: 243px;
    color: var(--white); font-weight: 500; font-size: 37px; line-height: 46px;
  }
  .ad-rectangle .brand-tile {
    position: absolute; left: 528px; top: 0; width: 124px; height: 134px;
    background: var(--white); display: flex; align-items: center; justify-content: center; gap: 6px;
  }
  .brand-name { color: var(--ink); font-weight: 500; font-size: 17px; line-height: 19px; text-align: left; }
  .brand-dot { width: 10px; height: 10px; border-radius: 50%; background: var(--maroon); flex: none; }

  .cta {
    position: absolute; display: flex; align-items: center; justify-content: space-between;
    background: linear-gradient(180deg, var(--orange) 0%, var(--orange-dark) 100%);
    border: 2px solid #f7a070; border-radius: 6px; color: var(--white); font-weight: 500;
  }
  .ad-rectangle .cta { left: 20px; top: 478px; width: 316px; height: 58px; padding: 0 16px; font-size: 32px; }
  .cta svg { flex: none; }

  /* ---------- Leaderboard ---------- */
  .ad-leaderboard {
    position: absolute; left: 62px; top: 915px; width: 1077px; height: 133px;
    background: var(--grey-band); overflow: hidden;
  }
  .ad-leaderboard .bands { position: absolute; inset: 0; }
  .ad-leaderboard .brand-tile {
    position: absolute; left: 0; top: 0; width: 150px; height: 133px;
    display: flex; align-items: center; justify-content: center; gap: 6px;
  }
  .ad-leaderboard .line-one {
    position: absolute; left: 202px; top: 10px; color: var(--white); font-weight: 600;
    font-size: 36px; line-height: 48px; letter-spacing: 2px; white-space: nowrap;
  }
  .ad-leaderboard .line-two {
    position: absolute; left: 178px; top: 76px; color: var(--white); font-weight: 600;
    font-size: 38px; line-height: 50px; letter-spacing: 1.2px; white-space: nowrap;
  }
  .accent { color: var(--gold); }
  .ad-leaderboard .cta { left: 762px; top: 46px; width: 186px; height: 35px; padding: 0 8px; font-size: 19px; border-radius: 4px; }
  .ad-leaderboard .hero-photo {
    position: absolute; left: 953px; top: 0; width: 124px; height: 133px;
    background:
      radial-gradient(ellipse 22px 55px at 62px 55px, rgba(47,76,120,0.9) 0%, rgba(63,95,143,0.5) 60%, rgba(79,109,150,0) 100%),
      radial-gradient(ellipse 48px 16px at 64px 110px, rgba(226,196,176,0.6) 0%, rgba(226,196,176,0) 100%),
      linear-gradient(90deg, var(--sky-light) 0%, var(--sky-mid) 40%, var(--sky-deep) 100%);
  }
</style>
</head>
<body>

<section class="ad-rectangle" aria-label="Medium rectangle ad">
  <div class="hero-photo" role="img" aria-label="Photo of a businessman in a blue suit holding a cluster of glass skyscrapers in his open palm"></div>
  <h1 class="headline">CLIENT<br>FOLLOW-UP<br>MADE SIMPLE</h1>
  <svg class="ribbon" viewBox="0 0 245 226" aria-hidden="true">
    <path d="M0 13 H242 Q218 113 238 213 H0 Z" fill="var(--steel)"/>
    <path d="M224 0 L242 13 H224 Z" fill="var(--maroon)"/>
    <path d="M224 226 L238 213 H224 Z" fill="var(--maroon)"/>
  </svg>
  <p class="ribbon-text">VIRTUALLY<br>NO COST<br>TO YOUR<br>COMPANY!</p>
  <div class="brand-tile"><span class="brand-dot"></span><span class="brand-name">Harborlyne<br>Works</span></div>
  <div class="cta">
    <svg width="34" height="34" viewBox="0 0 24 24" aria-hidden="true"><path fill="#fff" d="M6.6 10.8a15 15 0 0 0 6.6 6.6l2.2-2.2c.3-.3.7-.4 1-.2 1.1.4 2.3.6 3.6.6.6 0 1 .4 1 1V20c0 .6-.4 1-1 1A17 17 0 0 1 3 4c0-.6.4-1 1-1h3.5c.6 0 1 .4 1 1 0 1.2.2 2.4.6 3.6.1.3 0 .7-.2 1z"/><path d="M14 3a7 7 0 0 1 7 7M14 6.5a3.5 3.5 0 0 1 3.5 3.5" stroke="#fff" stroke-width="1.6" fill="none"/></svg>
    <span>CALL TO ACTION</span>
    <svg width="38" height="38" viewBox="0 0 24 24" aria-hidden="true"><circle cx="12" cy="12" r="10.5" fill="#fff"/><path d="M6.5 9.5h5.5V6l6 6-6 6v-3.5H6.5z" fill="var(--orange)"/></svg>
  </div>
</section>

<section class="ad-leaderboard" aria-label="Leaderboard ad">
  <svg class="bands" viewBox="0 0 1077 133" preserveAspectRatio="none" aria-hidden="true">
    <path d="M0 0 H182 L150 133 H0 Z" fill="var(--white)"/>
    <path d="M182 0 H806 L746 65 H138 Z" fill="var(--maroon)"/>
    <path d="M178 65 H890 L842 133 H145 Z" fill="var(--steel)"/>
  </svg>
  <div class="brand-tile"><span class="brand-dot"></span><span class="brand-name">Harborlyne<br>Works</span></div>
  <p class="line-one">CLIENT FOLLOW-UP <span class="accent">MADE SIMPLE</span></p>
  <p class="line-two">VIRTUALLY NO COST TO <span class="accent">YOUR COMPANY!</span></p>
  <div class="cta">
    <svg width="20" height="20" viewBox="0 0 24 24" aria-hidden="true"><path fill="#fff" d="M6.6 10.8a15 15 0 0 0 6.6 6.6l2.2-2.2c.3-.3.7-.4 1-.2 1.1.4 2.3.6 3.6.6.6 0 1 .4 1 1V20c0 .6-.4 1-1 1A17 17 0 0 1 3 4c0-.6.4-1 1-1h3.5c.6 0 1 .4 1 1 0 1.2.2 2.4.6 3.6.1.3 0 .7-.2 1z"/></svg>
    <span>CALL TO ACTION</span>
    <svg width="22" height="22" viewBox="0 0 24 24" aria-hidden="true"><circle cx="12" cy="12" r="10.5" fill="#fff"/><path d="M6.5 9.5h5.5V6l6 6-6 6v-3.5H6.5z" fill="var(--orange)"/></svg>
  </div>
  <div class="hero-photo" role="img" aria-label="Photo of a businessman holding a cluster of glass skyscrapers in his open palm"></div>
</section>

</body>
</html>
```